One page promotional flyer

Wanting a modern one page promotional flyer to promote our fire protection equipment and services . You can use stock images if desired .
Links to both from website below :

https://kvt-halvick.com/fire-protection/
https://kvt-halvick.com/fire-pump-service/

TY!

```html
<!DOCTYPE html>
<html lang="en">
<head>
<meta charset="utf-8">
<title>KVT Fire Protection Flyer</title>
<link href="https://fonts.googleapis.com/css2?family=Oswald:wght@500;700&family=Lato:wght@400;700&family=Roboto+Slab:wght@400&display=swap" rel="stylesheet">
<style>
  :root{
    --blue:#3a73c9;
    --blue-dark:#1f4e9c;
    --ink:#2b2b2b;
    --black:#1e1c1d;
    --paper:#f4f4f6;
    --bg:#d9d9d9;
    --white:#ffffff;
  }
  *{box-sizing:border-box;margin:0;padding:0}
  html,body{width:1200px;height:1200px;overflow:hidden;background:var(--bg)}
  .flyer{position:absolute;left:160px;top:30px;width:880px;height:1140px;background:var(--paper);overflow:hidden;font-family:"Lato",sans-serif;color:var(--ink)}
  .hero{position:absolute;left:0;top:0;width:880px;height:540px;
    background:linear-gradient(160deg,#d9d2c8 0%,#c9b8a8 30%,#b43a2c 55%,#8e1f18 80%,#c8402c 100%);
    clip-path:polygon(0 0,100% 0,100% 430px,0 530px)}
  .hero-band{position:absolute;left:0;top:0;width:880px;height:560px}
  .logo-area{position:absolute;left:0;top:0;width:330px;height:240px}
  .brand{position:absolute;left:52px;top:78px;display:flex;align-items:center;gap:10px;
    font-family:"Oswald",sans-serif;font-weight:700;font-size:64px;color:var(--blue-dark);letter-spacing:1px}
  .brand-dot{width:16px;height:16px;border-radius:50%;background:var(--blue-dark)}
  .headline{position:absolute;left:48px;top:300px;font-family:"Oswald",sans-serif;font-weight:700;
    font-size:44px;line-height:1.08;color:var(--white);text-transform:uppercase;
    text-shadow:0 3px 6px rgba(0,0,0,.6)}
  .product{position:absolute;border-radius:18px;background:radial-gradient(circle at 40% 40%,#e3343a,#a0141b 75%)}
  .product.one{left:520px;top:330px;width:150px;height:120px}
  .product.two{left:690px;top:300px;width:170px;height:125px}

  .col{position:absolute;display:flex;flex-direction:column}
  .col h2{font-family:"Oswald",sans-serif;font-weight:500;font-size:27px;color:var(--blue);margin-bottom:8px;line-height:1.1}
  .col p{font-size:10.6px;line-height:1.45;margin-bottom:9px;text-align:justify}
  .col-left{left:40px;top:560px;width:410px;height:510px}
  .col-right{left:470px;top:505px;width:380px;height:565px}
  .services{list-style:none;margin-bottom:12px}
  .services li{display:flex;align-items:center;gap:8px;font-size:10.8px;font-weight:700;line-height:1.75}
  .tick{width:12px;height:12px;flex:none}

  .tiles{flex:1;min-height:0;margin-top:6px;display:grid;grid-template-columns:1fr 1fr;grid-template-rows:repeat(4,1fr);gap:5px 8px}
  .tile{position:relative;overflow:hidden;background:linear-gradient(135deg,#9a1c18,#d7372e 50%,#6b6560)}
  .tile-label{position:absolute;left:0;right:0;bottom:0;height:20px;background:var(--blue);
    color:var(--white);font-family:"Roboto Slab",serif;font-size:13px;text-align:center;line-height:20px}
  .gallery{flex:1;min-height:0;display:grid;grid-template-columns:1fr 1fr;grid-template-rows:1fr 1fr;gap:6px}
  .gallery div{background:linear-gradient(135deg,#7a1814,#c33a2e 55%,#8b8580)}

  .footer{position:absolute;left:0;bottom:0;width:880px;height:62px;background:var(--black);
    display:flex;align-items:center;justify-content:space-around;color:var(--white);font-size:19px;letter-spacing:.5px}
  .contact{display:flex;align-items:center;gap:9px}
  .icon{width:24px;height:24px;flex:none}
</style>
</head>
<body>
<div class="flyer">
  <div class="hero" role="img" aria-label="Photo of a pump room with red fire pumps, piping and gauges"></div>
  <svg class="hero-band" viewBox="0 0 880 560" aria-hidden="true">
    <polygon points="0,530 880,430 880,442 0,542" fill="var(--blue)"/>
    <polygon points="0,542 880,442 880,560 0,560" fill="var(--paper)"/>
  </svg>
  <svg class="logo-area" viewBox="0 0 330 240" aria-hidden="true">
    <path d="M0 0 H330 C310 140 200 220 0 230 Z" fill="var(--white)"/>
    <path d="M330 0 C310 140 200 220 0 230" fill="none" stroke="var(--blue)" stroke-width="8"/>
  </svg>
  <div class="brand"><span class="brand-dot"></span>KVT</div>
  <div class="headline">Space-Saving<br>Fire Ptrotection<br>Solution</div>
  <div class="product one" role="img" aria-label="Red split-case fire pump product photo"></div>
  <div class="product two" role="img" aria-label="Red split-case fire pump product photo"></div>

  <section class="col col-left">
    <h2>Fire Protection Equipment</h2>
    <p>Kestrel Valve Technologies (KVT) reppresents Stalwart fire pumps and systems throughout the state of Virginia. With over 90 years of progressive Stalwart designing, engineering &amp; manufacturing, Stalwart pumps are proven with thousands of pump unit installations around the world. With proven success and an outstanding reputation Stalwart Pump is recognized as one of the leaders in this industry.</p>
    <p>Stalwart Pump designs tough, versatile products to meet your pumping needs. The fire pump units, systems, and housed packaged systems offer variety, durability, standardized options &amp; configurations true to their outstanding reputation. Thousands of Stalwart Pump installations (UL, ULC, or FM approved) deliver superior fire protection to facilities worldwide. Products are designed from a broad selection of pumps, drives, controls, baseplates and accessories.</p>
    <div class="tiles">
      <div class="tile" role="img" aria-label="Fire pump photo"><div class="tile-label">Fire Pumps</div></div>
      <div class="tile" role="img" aria-label="Jockey pumps photo"><div class="tile-label">Jockey Pumps</div></div>
      <div class="tile" role="img" aria-label="Electric motor photo"><div class="tile-label">Electric Motors</div></div>
      <div class="tile" role="img" aria-label="Diesel engine photo"><div class="tile-label">Diesel Engines</div></div>
      <div class="tile" role="img" aria-label="Pump controller cabinets photo"><div class="tile-label">Controllers</div></div>
      <div class="tile" role="img" aria-label="Skid package photo"><div class="tile-label">Skid Packages</div></div>
      <div class="tile" role="img" aria-label="Fully enclosed pump package photo"><div class="tile-label">Fully Enclosed Packages</div></div>
      <div class="tile" role="img" aria-label="Pump service and repair photo"><div class="tile-label">Service &amp; Repair</div></div>
    </div>
  </section>

  <section class="col col-right">
    <h2>Fire Pump Service</h2>
    <p>Our technicians have performed hundreds of pump repairs &amp; flow tests since our company's inception in 1981. We pride ourselves on doing the job right the first time, and appreciate the importance of getting a fire pump back into service.</p>
    <p>Our technicians are well versed in every fire pump make and model and the <b>fire pump parts</b> associated with any repair. We do not take the easy approach to repairing packing by using packing pullers, as some companies do. Every pump we work on is properly disassembled, inspected, cleaned, re-assembled &amp; test run. Whether your pump requires general maintenance or a complete overhaul, we have the knowledge, the quality fire pump parts, and the expertise to complete the job on time, and on budget.</p>
    <h2>Our Services Include:</h2>
    <ul class="services">
      <li><svg class="tick" viewBox="0 0 12 12"><rect x="0.5" y="0.5" width="11" height="11" fill="none" stroke="var(--blue)"/><path d="M2.5 6 L5 8.5 L10 2.5" fill="none" stroke="var(--blue)" stroke-width="2"/></svg>Fire pump repacks / overhaul / testing *most fire pump manufacturers</li>
      <li><svg class="tick" viewBox="0 0 12 12"><rect x="0.5" y="0.5" width="11" height="11" fill="none" stroke="var(--blue)"/><path d="M2.5 6 L5 8.5 L10 2.5" fill="none" stroke="var(--blue)" stroke-width="2"/></svg>Control panel troubleshooting &amp; repair (common makes &amp; models)</li>
      <li><svg class="tick" viewBox="0 0 12 12"><rect x="0.5" y="0.5" width="11" height="11" fill="none" stroke="var(--blue)"/><path d="M2.5 6 L5 8.5 L10 2.5" fill="none" stroke="var(--blue)" stroke-width="2"/></svg>Motor repair and replacement</li>
      <li><svg class="tick" viewBox="0 0 12 12"><rect x="0.5" y="0.5" width="11" height="11" fill="none" stroke="var(--blue)"/><path d="M2.5 6 L5 8.5 L10 2.5" fill="none" stroke="var(--blue)" stroke-width="2"/></svg>In-stock fire pump parts for all Stalwart / Norvik pumps</li>
      <li><svg class="tick" viewBox="0 0 12 12"><rect x="0.5" y="0.5" width="11" height="11" fill="none" stroke="var(--blue)"/><path d="M2.5 6 L5 8.5 L10 2.5" fill="none" stroke="var(--blue)" stroke-width="2"/></svg>Jockey pumps and jockey pump controllers in stock</li>
      <li><svg class="tick" viewBox="0 0 12 12"><rect x="0.5" y="0.5" width="11" height="11" fill="none" stroke="var(--blue)"/><path d="M2.5 6 L5 8.5 L10 2.5" fill="none" stroke="var(--blue)" stroke-width="2"/></svg>Testing equipment: Hoses, Pitot tubes, tachometers</li>
    </ul>
    <div class="gallery">
      <div role="img" aria-label="Red fire pump installation photo"></div>
      <div role="img" aria-label="Disassembled pump rotor photo"></div>
      <div role="img" aria-label="Pump room service work photo"></div>
      <div role="img" aria-label="Pump casing being repaired photo"></div>
    </div>
  </section>

  <footer class="footer">
    <div class="contact">
      <svg class="icon" viewBox="0 0 24 24"><circle cx="12" cy="12" r="12" fill="var(--blue)"/><path d="M8 6 L10.5 6 L11.5 9 L10 10.2 C10.8 12 12 13.2 13.8 14 L15 12.5 L18 13.5 L18 16 C12 17 7 12 8 6 Z" fill="var(--white)"/></svg>
      <span>(555)013-7200</span>
    </div>
    <div class="contact">
      <svg class="icon" viewBox="0 0 24 24"><circle cx="12" cy="12" r="12" fill="var(--blue)"/><rect x="6" y="8" width="12" height="8" fill="none" stroke="var(--white)" stroke-width="1.5"/><path d="M6 8 L12 13 L18 8" fill="none" stroke="var(--white)" stroke-width="1.5"/></svg>
      <span>sales@kvt-halvick.com</span>
    </div>
    <div class="contact">
      <svg class="icon" viewBox="0 0 24 24"><circle cx="12" cy="12" r="12" fill="var(--blue)"/><circle cx="12" cy="12" r="6" fill="none" stroke="var(--white)" stroke-width="1.4"/><ellipse cx="12" cy="12" rx="2.6" ry="6" fill="none" stroke="var(--white)" stroke-width="1.2"/><path d="M6 12 H18" stroke="var(--white)" stroke-width="1.2"/></svg>
      <span>www.kvt-halvick.com</span>
    </div>
  </footer>
</div>
</body>
</html>
```